Search Fund needs a PowerPoint template design

We need a eye-catching and compelling PowerPoint design for a new company based in Chicago called Harrow Ridge Partners. We are search fund with a primary mission to acquire a founder/family/entrepreneur owned businesses (This is similar to a Private Equity firm). Our goal is to offer investors a unique avenue to invest in an attractive business acquisition while providing business owners with an alternative path to exit. We would like the design to reflect crisp and professional nature that many financial firms present. The template should build on the design of the logo including expanding a logical color palette. The presentation will be used to describe facts regarding the firm, financial data and key messaging that we want our investors and potential partners to takeaway.

Target Market(s)

Financial Investors

Industry/Entity Type

Finance

Font styles to use
Serif
Sans Serif

Colors

Designer to choose colors to be used in the design.

Requirements
Must have
• Should include cover page and slide examples. Attractive data displays (graphs, charts, infographics etc.); Compelling cover; fly pages to put in between sections; table of contents page. Needs to have white space to add text.
Should not have
• Do not redesign the logo or change the logo colors. Additional colors should be added to the PowerPoint template

```html
<!DOCTYPE html>
<html lang="en">
<head>
<meta charset="utf-8">
<title>Harrow Ridge Partners – Presentation Template</title>
<link href="https://fonts.googleapis.com/css2?family=Montserrat:wght@500;600;700&family=Raleway:ital,wght@0,300;0,400;0,600;0,700;1,300;1,400&display=swap" rel="stylesheet">
<style>
  :root{
    --blue:#1f6fc1;
    --blue-light:#4a8fd4;
    --navy:#1f3c66;
    --ink:#2e2e2e;
    --gray:#8c8c8c;
    --soft:#b9b9b9;
    --line:#d9d9d9;
    --canvas:#e9e9ea;
    --white:#ffffff;
  }
  *{box-sizing:border-box;margin:0;padding:0}
  html,body{width:1200px;height:866px;overflow:hidden;background:var(--canvas)}
  body{font-family:"Raleway",sans-serif;color:var(--ink)}
  .deck{display:grid;grid-template-columns:repeat(4,290px);grid-template-rows:repeat(5,163.5px);gap:8px;padding:8px;width:1200px;height:866px}
  .slide{position:relative;background:var(--white);overflow:hidden;box-shadow:0 1px 2px rgba(0,0,0,.12)}
  .edge{position:absolute;left:0;top:0;bottom:0;width:6px;background:var(--blue)}
  .num{position:absolute;top:7px;right:8px;width:10px;height:12px;background:var(--blue);color:#fff;font:600 3.6px "Montserrat",sans-serif;display:flex;align-items:center;justify-content:center}
  .brand{position:absolute;right:9px;bottom:5px;font:700 3.4px "Raleway",sans-serif;color:var(--blue);letter-spacing:.1px}
  .title{position:absolute;left:22px;top:13px;font:700 6.6px "Montserrat",sans-serif;color:#6a6a6a;letter-spacing:.2px}
  .t{font-size:3.3px;line-height:1.55;color:#9a9a9a}
  .t b{color:var(--ink)}
  .lead{font-size:3.9px;line-height:1.5;color:#777}
  .lead b{color:var(--ink)}
  .photo{position:absolute}
  .abs{position:absolute}
  .ico-row{display:flex;justify-content:space-between}
  .circ{border-radius:50%;display:flex;align-items:center;justify-content:center}
  .lbl{font:600 3.6px "Montserrat",sans-serif;color:#444;text-align:center}
  .cols{display:flex;gap:10px}
  .cols>div{flex:1}
  .bar-row{display:grid;grid-template-columns:2fr 1fr 1fr 1fr 1fr;padding:1.6px 0;border-bottom:.4px solid #ddd}
</style>
</head>
<body>
<main class="deck">

  <!-- 1 cover -->
  <section class="slide cover">
    <div class="edge"></div>
    <div class="photo" role="img" aria-label="Photo of a white desk with coffee cup, glasses and keyboard" style="left:150px;top:0;right:0;bottom:0;background:linear-gradient(135deg,#f7f7f7 0%,#e4e4e4 55%,#cfd2d5 100%)"></div>
    <div class="abs" style="left:38px;top:72px;font:700 7px 'Raleway',sans-serif;color:var(--blue)">Harrow Ridge Partners</div>
    <div class="abs" style="left:38px;top:90px;font:600 9.5px 'Raleway',sans-serif;color:#555">Presentation Template</div>
    <div class="abs" style="left:38px;top:102px;font:400 5px 'Raleway',sans-serif;color:var(--blue)">Some description of subtitle here</div>
    <div class="abs" style="left:38px;top:115px;width:108px;height:8px;border-radius:4px;background:#a9a9a9;color:#fff;font-size:3.6px;display:flex;align-items:center;justify-content:center">www.harrowridge.example</div>
  </section>

  <!-- 2 contents -->
  <section class="slide">
    <div class="photo" role="img" aria-label="Photo of a presenter at a whiteboard in an office" style="left:0;top:0;width:122px;bottom:0;background:linear-gradient(160deg,#f1efec,#d9d4cd 60%,#b9b2a8)"></div>
    <div class="abs" style="left:122px;top:0;width:16px;bottom:0;background:#a9a9a9"></div>
    <div class="abs" style="left:16px;top:10px;font:700 6.4px 'Montserrat',sans-serif;color:#666">CONTENT AT GLANCE</div>
    <div class="num">2</div>
    <div class="abs" style="left:124px;top:44px;right:12px">
      <div style="display:grid;grid-template-columns:14px 1fr 10px;row-gap:6.1px;font-size:3.8px;color:#999">
        <span>01</span><span>Self-Awareness</span><span>01</span>
        <span>02</span><span>Professional Integrity</span><span>02</span>
        <span>03</span><span>Leadership in The Entry Level</span><span>03</span>
        <span>04</span><span>Trust, Accountability &amp; Reliability</span><span>04</span>
        <span>05</span><span>The Value of Questions</span><span>05</span>
        <span>06</span><span>Owning Mistakes</span><span>06</span>
        <span>07</span><span>Resilience in the Face of Challenges</span><span>07</span>
        <span>08</span><span>Valuing Your Strengths</span><span>08</span>
      </div>
    </div>
    <div class="brand">HARROW RIDGE</div>
  </section>

  <!-- 3 agenda -->
  <section class="slide">
    <div class="edge"></div><div class="num">3</div>
    <div class="title">PRESENTATION AGENDA</div>
    <div class="abs" style="left:38px;top:50px;right:40px;display:grid;grid-template-columns:repeat(3,1fr);row-gap:14px;column-gap:10px">
      <div><svg width="20" height="7"><path d="M0 0H17L20 3.5L17 7H0Z" fill="#2c5a8c"/><text x="4" y="5" font-size="3.6" fill="#fff" font-family="Montserrat">01</text></svg><p class="t" style="margin-top:3px">Contrary to popular belief, it is not simply random text.</p></div>
      <div><svg width="20" height="7"><path d="M0 0H17L20 3.5L17 7H0Z" fill="#2c5a8c"/><text x="4" y="5" font-size="3.6" fill="#fff" font-family="Montserrat">02</text></svg><p class="t" style="margin-top:3px">Contrary to popular belief, it is not simply random text.</p></div>
      <div><svg width="20" height="7"><path d="M0 0H17L20 3.5L17 7H0Z" fill="#2c5a8c"/><text x="4" y="5" font-size="3.6" fill="#fff" font-family="Montserrat">03</text></svg><p class="t" style="margin-top:3px">Contrary to popular belief, it is not simply random text.</p></div>
      <div><svg width="20" height="7"><path d="M0 0H17L20 3.5L17 7H0Z" fill="#2c5a8c"/><text x="4" y="5" font-size="3.6" fill="#fff" font-family="Montserrat">04</text></svg><p class="t" style="margin-top:3px">Contrary to popular belief, it is not simply random text.</p></div>
      <div><svg width="20" height="7"><path d="M0 0H17L20 3.5L17 7H0Z" fill="#2c5a8c"/><text x="4" y="5" font-size="3.6" fill="#fff" font-family="Montserrat">05</text></svg><p class="t" style="margin-top:3px">Contrary to popular belief, it is not simply random text.</p></div>
      <div><svg width="20" height="7"><path d="M0 0H17L20 3.5L17 7H0Z" fill="#2c5a8c"/><text x="4" y="5" font-size="3.6" fill="#fff" font-family="Montserrat">06</text></svg><p class="t" style="margin-top:3px">Contrary to popular belief, it is not simply random text.</p></div>
    </div>
    <div class="brand">HARROW RIDGE</div>
  </section>

  <!-- 4 board intro -->
  <section class="slide">
    <div class="photo" role="img" aria-label="Portrait photo of the chief executive officer at her desk" style="left:0;top:0;width:130px;bottom:0;background:linear-gradient(150deg,#e9e4de,#c8b9a6 55%,#a59583)"></div>
    <div class="num">4</div>
    <div class="abs" style="left:132px;top:14px;font:700 6.4px 'Montserrat',sans-serif;color:var(--blue)">BOARD INTRODUCTION</div>
    <div class="abs" style="left:132px;top:36px;right:24px;border-bottom:.6px solid #999;padding-bottom:3px;font-size:7.5px;color:#444">Welcome from <b>Marisa</b></div>
    <div class="abs" style="left:132px;top:52px;font-size:3.6px;color:var(--blue)">President and Chief Executive Officer</div>
    <div class="abs t" style="left:132px;top:66px;right:22px">Marisa joined us to lead a new chapter for the firm and its partners. Our focus stays on careful acquisitions, steady growth and long term value for every investor who places trust in the team.<br><br>We work closely with founders and families to plan each transition with care, keeping their people, customers and legacy at the centre of every decision we take together.</div>
    <div class="brand">HARROW RIDGE</div>
  </section>

  <!-- 5 about -->
  <section class="slide">
    <div class="edge"></div><div class="num">5</div>
    <div class="title">ABOUT US</div>
    <div class="abs t" style="left:56px;top:32px;right:60px">Our firm was formed to acquire and grow one strong, owner led business. We bring patient capital, operating focus and a clear plan for the years after the transition.<br><br>Investors gain direct access to a single <span style="color:var(--blue)">operating company</span> while sellers receive a fair path to exit. Our team is based in Chicago and works with owners across the Midwest and wider US.</div>
    <div class="abs" style="left:56px;top:81px;width:176px;height:8px;border-radius:4px;background:var(--blue);color:#fff;font-size:4px;display:flex;align-items:center;justify-content:center">VALUE PROPOSITION</div>
    <div class="abs ico-row" style="left:60px;top:100px;width:168px">
      <div><div class="circ" style="width:14px;height:14px;margin:0 auto;background:#9b9b9b"><svg width="7" height="7" viewBox="0 0 10 10"><circle cx="5" cy="4" r="3" fill="none" stroke="#fff"/><path d="M4 8h2" stroke="#fff"/></svg></div><p class="lbl" style="margin-top:6px">The Subtitle</p></div>
      <div><div class="circ" style="width:14px;height:14px;margin:0 auto;background:#9b9b9b"><svg width="7" height="7" viewBox="0 0 10 10"><path d="M2 2v6M5 2v6M8 2v6" stroke="#fff"/></svg></div><p class="lbl" style="margin-top:6px">The Subtitle</p></div>
      <div><div class="circ" style="width:14px;height:14px;margin:0 auto;background:#9b9b9b"><svg width="7" height="7" viewBox="0 0 10 10"><path d="M2 8L8 2" stroke="#fff" stroke-width="1.5"/></svg></div><p class="lbl" style="margin-top:6px">The Subtitle</p></div>
      <div><div class="circ" style="width:14px;height:14px;margin:0 auto;background:#9b9b9b"><svg width="7" height="7" viewBox="0 0 10 10"><path d="M1 5L9 1L6 9L5 6Z" fill="#fff"/></svg></div><p class="lbl" style="margin-top:6px">The Subtitle</p></div>
    </div>
    <div class="brand">HARROW RIDGE</div>
  </section>

  <!-- 6 statement -->
  <section class="slide">
    <div class="photo" role="img" aria-label="Black and white photo of a modern glass office tower" style="inset:0;background:linear-gradient(115deg,#8f8f8f 0%,#d0d0d0 35%,#f4f4f4 60%,#ffffff 100%)"></div>
    <div class="num">6</div>
    <div class="circ abs" style="left:205px;top:42px;width:17px;height:17px;background:var(--blue)"><svg width="8" height="7" viewBox="0 0 8 7"><path d="M0 7V3L2 0H3L2 3H3.5V7ZM4.5 7V3L6.5 0H7.5L6.5 3H8V7Z" fill="#fff"/></svg></div>
    <div class="abs" style="left:150px;right:10px;top:66px;text-align:center;font:italic 400 7px 'Raleway',sans-serif;color:#666">Business that <b style="font-weight:600">Advances</b></div>
    <div class="abs" style="left:146px;right:10px;top:86px;text-align:center;font:italic 300 6px/1.25 'Raleway',sans-serif;color:var(--blue)">Sustainable and innovative solutions that help achieve environmental, design, and engineering goals</div>
    <div class="brand">HARROW RIDGE</div>
  </section>

  <!-- 7 operation -->
  <section class="slide">
    <div class="edge"></div><div class="num">7</div>
    <div class="title">OPERATION PRINCIPLES</div>
    <div class="abs" style="left:60px;right:55px;top:46px;display:flex;justify-content:space-between;align-items:flex-start">
      <div style="width:50px;text-align:center">
        <div class="circ" style="width:36px;height:36px;margin:4px auto 0;background:#111"><svg width="14" height="12" viewBox="0 0 14 12"><rect x="1" y="3" width="12" height="8" rx="1" fill="#fff"/><rect x="5" y="1" width="4" height="3" fill="none" stroke="#fff"/></svg></div>
        <p class="lbl" style="margin-top:6px;font-size:4.6px">Vision</p>
        <p class="t" style="margin-top:2px">We value direct partners who share our long view</p>
      </div>
      <div style="width:58px;text-align:center">
        <div class="circ" style="width:46px;height:46px;margin:0 auto;border:1.2px solid var(--blue);padding:2px"><div class="circ" style="width:100%;height:100%;background:var(--blue)"><svg width="18" height="16" viewBox="0 0 18 16"><path d="M1 5L9 1L17 5Z" fill="#fff"/><path d="M3 6v7M7 6v7M11 6v7M15 6v7" stroke="#fff" stroke-width="1.6"/><rect x="1" y="14" width="16" height="1.5" fill="#fff"/></svg></div></div>
        <p class="lbl" style="margin-top:3px;font-size:4.6px">Core Values</p>
        <p class="t" style="margin-top:2px">Trust, care and discipline guide every step we take</p>
      </div>
      <div style="width:50px;text-align:center">
        <div class="circ" style="width:36px;height:36px;margin:4px auto 0;background:#111"><svg width="16" height="12" viewBox="0 0 16 12"><path d="M0 4L8 0L16 4L8 8Z" fill="#fff"/><path d="M4 6v3q4 3 8 0V6" fill="#fff"/></svg></div>
        <p class="lbl" style="margin-top:6px;font-size:4.6px">Mission</p>
        <p class="t" style="margin-top:2px">We grow one great company with its people</p>
      </div>
    </div>
    <div class="brand">HARROW RIDGE</div>
  </section>

  <!-- 8 icon strategy -->
  <section class="slide">
    <div class="edge"></div><div class="num">8</div>
    <div class="title">ICON STRATEGY LIST</div>
    <div class="abs t" style="left:22px;right:14px;top:30px;color:#555">Lorem ipsum dolor sit amet, consectetur adipiscing elit. Through our high performance, low CO<sub>2</sub> concrete, more <b style="color:var(--blue)">Technology</b> and Control Concrete Sustainability Specialist (CSS), we continue to contribute to the building of projects that are environmentally responsible and cost effective and healthy places to live and work.</div>
    <div class="abs ico-row" style="left:26px;right:20px;top:60px">
      <div style="width:30px;text-align:center"><div class="circ" style="width:15px;height:15px;margin:0 auto;border:.6px solid #888"><svg width="7" height="7"><circle cx="3.5" cy="3.5" r="2.5" fill="none" stroke="#666" stroke-width=".6"/></svg></div><p style="font-size:3.2px;color:var(--blue);margin-top:3px">CO2 reduction</p><p class="t">Lower output and better mix</p></div>
      <div style="width:30px;text-align:center"><div class="circ" style="width:15px;height:15px;margin:0 auto;border:.6px solid #888"><svg width="7" height="7"><path d="M1 4a2.5 2.5 0 1 0 2.5-2.5" fill="none" stroke="#666" stroke-width=".6"/></svg></div><p style="font-size:3.2px;color:var(--blue);margin-top:3px">Recyclable</p><p class="t">Reuse of site material</p></div>
      <div style="width:30px;text-align:center"><div class="circ" style="width:15px;height:15px;margin:0 auto;border:.6px solid #888"><svg width="7" height="7"><rect x="1" y="1" width="5" height="5" fill="none" stroke="#666" stroke-width=".6"/></svg></div><p style="font-size:3.2px;color:var(--blue);margin-top:3px">Cost benefit</p><p class="t">Lower cost over building life</p></div>
      <div style="width:30px;text-align:center"><div class="circ" style="width:15px;height:15px;margin:0 auto;border:.6px solid #888"><svg width="7" height="7"><path d="M1 6L6 1" stroke="#666" stroke-width=".6"/></svg></div><p style="font-size:3.2px;color:var(--blue);margin-top:3px">Reduced waste</p><p class="t">Less waste at each site</p></div>
      <div style="width:30px;text-align:center"><div class="circ" style="width:15px;height:15px;margin:0 auto;border:.6px solid #888"><svg width="7" height="7"><circle cx="3.5" cy="3.5" r="1.5" fill="none" stroke="#666" stroke-width=".6"/></svg></div><p style="font-size:3.2px;color:var(--blue);margin-top:3px">Energy efficiency</p><p class="t">Lower use of power</p></div>
      <div style="width:30px;text-align:center"><div class="circ" style="width:15px;height:15px;margin:0 auto;border:.6px solid #888"><svg width="7" height="7"><path d="M1 2h5M1 5h5" stroke="#666" stroke-width=".6"/></svg></div><p style="font-size:3.2px;color:var(--blue);margin-top:3px">Durability</p><p class="t">Built to last for decades</p></div>
    </div>
    <div class="abs" style="left:22px;right:14px;top:120px;height:6px;background:var(--blue);color:#fff;font:700 3.6px 'Montserrat',sans-serif;padding:1.3px 2px">CONCRETE IS THE FUTURE OF SUSTAINABLE CONSTRUCTION</div>
    <div class="abs t" style="left:22px;right:14px;top:128px;color:#666">Increasingly, concrete is being recognised for its life cycle environmental and economic benefits, from construction to operation, maintenance and disposal. There is a solid base that makes concrete the right choice for effective development.</div>
    <div class="brand">HARROW RIDGE</div>
  </section>

  <!-- 9 process -->
  <section class="slide">
    <div class="edge"></div><div class="num">9</div>
    <div class="title">THE PROCESS</div>
    <div class="abs" style="left:6px;right:0;top:30px;height:54px;background:#f1f1f1"></div>
    <div class="abs" style="left:24px;right:20px;top:36px;display:flex;align-items:flex-start;justify-content:space-between">
      <div style="width:34px;text-align:center"><svg width="12" height="8"><path d="M1 7a5 5 0 0 1 10 0" fill="none" stroke="#555"/><path d="M6 7L8 3" stroke="#555"/></svg><p class="t" style="color:#666">Phase one review of the company <b>sourcing</b></p></div>
      <svg width="24" height="8" style="margin-top:2px"><path d="M0 3H18V0L24 4L18 8V5H0Z" fill="var(--blue)"/></svg>
      <div style="width:34px;text-align:center"><svg width="10" height="9"><path d="M1 1L9 8M9 1L1 8" stroke="#555"/></svg><p class="t" style="color:#666">Phase two review of the company <b>diligence</b></p></div>
      <svg width="24" height="8" style="margin-top:2px"><path d="M0 3H18V0L24 4L18 8V5H0Z" fill="var(--blue)"/></svg>
      <div style="width:34px;text-align:center"><svg width="10" height="9"><circle cx="5" cy="4.5" r="3.5" fill="none" stroke="#555"/></svg><p class="t" style="color:#666">Phase three review of the company <b>closing</b></p></div>
      <svg width="24" height="8" style="margin-top:2px"><path d="M0 3H18V0L24 4L18 8V5H0Z" fill="var(--blue)"/></svg>
      <div style="width:34px;text-align:center"><svg width="12" height="9"><circle cx="3" cy="7" r="1.5" fill="#555"/><circle cx="9" cy="7" r="1.5" fill="#555"/><path d="M2 5h8V2" stroke="#555" fill="none"/></svg><p class="t" style="color:#666">Phase four review of the company <b>growth</b></p></div>
    </div>
    <div class="abs" style="left:18px;top:90px;width:110px;font:700 5.6px 'Raleway',sans-serif;color:#222;border-bottom:.6px solid #222;padding-bottom:2px">Subheading Description</div>
    <div class="abs t" style="left:20px;top:103px;width:100px;color:#777">
      <div>✓ Lorem ipsum dolor sit amet, ligula nunc diam</div>
      <div>✓ Fusce ut elit rhoncus tempor lorem sem</div>
      <div>✓ Lorem ipsum dolor sit amet, ligula nunc diam</div>
      <div>✓ Nulla pretium dapibus rhoncus tempor lorem</div>
      <div style="margin-top:3px">Lorem ipsum dolor sit amet, consectetur adipiscing elit. Nunc at nisi ut lorem nec fermentum vitae nisi ut nunc.</div>
    </div>
    <svg class="abs" style="left:140px;top:88px" width="125" height="66" viewBox="0 0 140 68">
      <g font-size="3" fill="#777" font-family="Raleway">
        <text x="0" y="4">6</text><text x="0" y="14">5</text><text x="0" y="24">4</text><text x="0" y="34">3</text><text x="0" y="44">2</text><text x="0" y="54">1</text><text x="0" y="64">0</text>
        <text x="22" y="67">2013</text><text x="52" y="67">2014</text><text x="82" y="67">2015</text><text x="112" y="67">2016</text>
      </g>
      <rect x="18" y="30" width="4" height="33" fill="#1f3c66"/><rect x="23" y="40" width="4" height="23" fill="#4a8fd4"/><rect x="28" y="48" width="4" height="15" fill="#a9a9a9"/>
      <rect x="48" y="40" width="4" height="23" fill="#1f3c66"/><rect x="53" y="28" width="4" height="35" fill="#4a8fd4"/><rect x="58" y="48" width="4" height="15" fill="#a9a9a9"/>
      <rect x="78" y="42" width="4" height="21" fill="#1f3c66"/><rect x="83" y="34" width="4" height="29" fill="#4a8fd4"/><rect x="88" y="24" width="4" height="39" fill="#a9a9a9"/>
      <rect x="108" y="24" width="4" height="39" fill="#1f3c66"/><rect x="113" y="34" width="4" height="29" fill="#4a8fd4"/><rect x="118" y="18" width="4" height="45" fill="#a9a9a9"/>
    </svg>
    <div class="brand">HARROW RIDGE</div>
  </section>

  <!-- 10 solutions -->
  <section class="slide">
    <div class="edge"></div><div class="num">10</div>
    <div class="title">OUR SOLUTIONS</div>
    <div class="abs" style="left:20px;top:38px;width:130px;height:110px;display:grid;grid-template-columns:1fr 1fr;grid-template-rows:1fr 1fr;border:.6px solid #bbb">
      <div style="border-right:.6px solid #bbb;border-bottom:.6px solid #bbb;display:flex;flex-direction:column;align-items:center;justify-content:center;gap:4px;font-size:4px;color:#777;text-align:center"><svg width="9" height="8"><path d="M0 1h3l3 6h3M0 7h3l3-6h3" stroke="#777" fill="none" stroke-width=".7"/></svg>Ready-Mixed<br>Concrete</div>
      <div style="border-bottom:.6px solid #bbb;display:flex;flex-direction:column;align-items:center;justify-content:center;gap:4px;font-size:4px;color:#777;text-align:center"><svg width="8" height="9"><rect x=".5" y=".5" width="7" height="8" fill="none" stroke="var(--blue)" stroke-width=".7"/><path d="M2 3h4M2 5h4" stroke="var(--blue)" stroke-width=".6"/></svg>Ready-Mixed<br>Concrete</div>
      <div style="border-right:.6px solid #bbb;display:flex;flex-direction:column;align-items:center;justify-content:center;gap:4px;font-size:4px;color:#777;text-align:center"><svg width="9" height="9"><circle cx="4" cy="4" r="3" fill="none" stroke="var(--blue)" stroke-width=".7"/><path d="M6 6l3 3" stroke="var(--blue)"/></svg>Value-Added<br>Services</div>
      <div style="display:flex;flex-direction:column;align-items:center;justify-content:center;gap:4px;font-size:4px;color:#777;text-align:center"><svg width="9" height="9"><path d="M4.5 .5l1.2 2.6 2.8.3-2.1 1.9.6 2.8-2.5-1.4-2.5 1.4.6-2.8L.5 3.4l2.8-.3z" fill="none" stroke="#999" stroke-width=".6"/></svg>Value-Added<br>Services</div>
    </div>
    <div class="abs" style="left:164px;right:18px;top:38px">
      <p style="font:700 4.4px 'Raleway',sans-serif">Ready-Mixed Concrete</p><p class="t" style="margin-bottom:5px">We produce mixes for every project size and deliver them on time across the region with care and steady quality control.</p>
      <p style="font:700 4.4px 'Raleway',sans-serif">Aggregates</p><p class="t" style="margin-bottom:5px">We produce mixes for every project size and deliver them on time across the region with care and steady quality control.</p>
      <p style="font:700 4.4px 'Raleway',sans-serif">Value-Added Services</p><p class="t" style="margin-bottom:5px">We produce mixes for every project size and deliver them on time across the region with care and steady quality control.</p>
      <p style="font:700 4.4px 'Raleway',sans-serif">Specialty Products/Solutions</p><p class="t">We produce mixes for every project size and deliver them on time across the region with care.</p>
    </div>
    <div class="brand">HARROW RIDGE</div>
  </section>

  <!-- 11 list point services -->
  <section class="slide">
    <div class="edge"></div><div class="num">11</div>
    <div class="title">LIST POINT SERVICES</div>
    <div class="abs" style="left:26px;right:26px;top:40px;display:grid;grid-template-columns:repeat(4,1fr);row-gap:10px;column-gap:10px;text-align:center">
      <div><div class="circ" style="width:16px;height:16px;margin:0 auto;background:var(--navy)"><svg width="6" height="6"><circle cx="3" cy="3" r="2" fill="#fff"/></svg></div><p style="font:600 3.2px 'Montserrat',sans-serif;margin-top:4px">Item | Subtitle Here</p><p class="t">Short line of service detail for the item shown</p></div>
      <div><div class="circ" style="width:16px;height:16px;margin:0 auto;background:#8a8a8a"><svg width="6" height="6"><rect x="1" y="1" width="4" height="4" fill="#fff"/></svg></div><p style="font:600 3.2px 'Montserrat',sans-serif;margin-top:4px">Item | Subtitle Here</p><p class="t">Short line of service detail for the item shown</p></div>
      <div><div class="circ" style="width:16px;height:16px;margin:0 auto;background:#b4b4b4"><svg width="6" height="6"><path d="M1 5L5 1" stroke="#fff"/></svg></div><p style="font:600 3.2px 'Montserrat',sans-serif;margin-top:4px">Item | Subtitle Here</p><p class="t">Short line of service detail for the item shown</p></div>
      <div><div class="circ" style="width:16px;height:16px;margin:0 auto;background:var(--blue-light)"><svg width="6" height="6"><circle cx="3" cy="3" r="2" fill="none" stroke="#fff"/></svg></div><p style="font:600 3.2px 'Montserrat',sans-serif;margin-top:4px">Item | Subtitle Here</p><p class="t">Short line of service detail for the item shown</p></div>
      <div><div class="circ" style="width:16px;height:16px;margin:0 auto;background:var(--blue-light)"><svg width="6" height="6"><circle cx="3" cy="3" r="1.5" fill="#fff"/></svg></div><p style="font:600 3.2px 'Montserrat',sans-serif;margin-top:4px">Item | Subtitle Here</p><p class="t">Short line of service detail for the item shown</p></div>
      <div><div class="circ" style="width:16px;height:16px;margin:0 auto;background:var(--navy)"><svg width="6" height="6"><path d="M1 5V3M3 5V1M5 5V2" stroke="#fff"/></svg></div><p style="font:600 3.2px 'Montserrat',sans-serif;margin-top:4px">Item | Subtitle Here</p><p class="t">Short line of service detail for the item shown</p></div>
      <div><div class="circ" style="width:16px;height:16px;margin:0 auto;background:#8a8a8a"><svg width="6" height="6"><rect x="1" y="1.5" width="4" height="3" fill="none" stroke="#fff"/></svg></div><p style="font:600 3.2px 'Montserrat',sans-serif;margin-top:4px">Item | Subtitle Here</p><p class="t">Short line of service detail for the item shown</p></div>
      <div><div class="circ" style="width:16px;height:16px;margin:0 auto;background:#b4b4b4"><svg width="6" height="6"><path d="M1 5L3 3L5 4L5 1" stroke="#fff" fill="none"/></svg></div><p style="font:600 3.2px 'Montserrat',sans-serif;margin-top:4px">Item | Subtitle Here</p><p class="t">Short line of service detail for the item shown</p></div>
    </div>
    <div class="brand">HARROW RIDGE</div>
  </section>

  <!-- 12 US map -->
  <section class="slide">
    <div class="edge"></div><div class="num">12</div>
    <div class="title">US MAPS</div>
    <div class="abs" style="left:22px;top:48px;width:80px">
      <p style="font:700 4.2px/1.3 'Raleway',sans-serif">Ut wisi enim ad minim<br>veniam, quis nostrud exerci</p>
      <p class="t" style="margin-top:3px">Our target companies sit in the heart of the country, with strong local roots, loyal clients and steady cash flow built over decades of work.</p>
      <div style="margin-top:10px;width:22px;height:4px;border-radius:2px;background:var(--blue)"></div>
    </div>
    <div class="photo" role="img" aria-label="Map of the United States with highlighted state and location pins" style="left:120px;top:42px;width:150px;height:95px;border-radius:4px;background:linear-gradient(180deg,#dcdcdc,#c9c9c9)"></div>
    <div class="abs" style="left:210px;top:48px;width:44px;height:10px;background:var(--blue);color:#fff;font-size:2.6px;padding:1.5px 2px;line-height:1.3">Our location and the main region we serve</div>
    <div class="brand">HARROW RIDGE</div>
  </section>

  <!-- 13 world map -->
  <section class="slide">
    <div class="edge"></div><div class="num">13</div>
    <div class="title">WORLD MAPS</div>
    <div class="photo" role="img" aria-label="World map with highlighted regions in blue" style="left:20px;top:44px;width:150px;height:86px;border-radius:4px;background:linear-gradient(120deg,#3b4c66,#7d8fa8 45%,#b8b8b8)"></div>
    <div class="abs" style="left:180px;top:30px;bottom:30px;border-left:.6px dashed #444"></div>
    <div class="abs" style="left:188px;top:42px;right:14px;display:grid;grid-template-columns:1fr 1fr;row-gap:20px">
      <div><p style="font:300 10px 'Raleway',sans-serif;color:var(--blue);line-height:1">15%</p><p style="font:700 4px 'Montserrat',sans-serif">Europe</p><p class="t">Share of firms in this area</p></div>
      <div><p style="font:300 10px 'Raleway',sans-serif;color:#888;line-height:1">30%</p><p style="font:700 4px 'Montserrat',sans-serif">US</p><p class="t">Share of firms in this area</p></div>
      <div><p style="font:300 10px 'Raleway',sans-serif;color:var(--blue);line-height:1">20%</p><p style="font:700 4px 'Montserrat',sans-serif">Africa</p><p class="t">Share of firms in this area</p></div>
      <div><p style="font:300 10px 'Raleway',sans-serif;color:#888;line-height:1">35%</p><p style="font:700 4px 'Montserrat',sans-serif">Asia</p><p class="t">Share of firms in this area</p></div>
    </div>
    <div class="brand">HARROW RIDGE</div>
  </section>

  <!-- 14 single list -->
  <section class="slide">
    <div class="edge"></div><div class="num">14</div>
    <div class="title">TRADITIONAL SINGLE LIST</div>
    <div class="abs lead" style="left:22px;right:40px;top:28px"><b style="color:var(--blue)">Contrary to popular belief,</b> Lorem Ipsum is not simply random text. It has roots in a piece of classical Latin literature from 45 BC</div>
    <div class="abs" style="left:22px;right:40px;top:46px;border-top:.6px solid var(--blue)"></div>
    <div class="abs t" style="left:38px;right:40px;top:60px;color:#777">
      <div style="display:flex;gap:5px;margin-bottom:4px"><svg width="6" height="6" style="flex:none"><path d="M.5 3L2.5 5L5.5 .5" stroke="var(--blue)" fill="none" stroke-width=".8"/></svg><span>Quisque libero dolor, bibendum nec quam sit amet, porta imperdiet ex. Aliquam at volutpat nisl. Quisque commodo ultricies mauris vel dignissim.</span></div>
      <div style="display:flex;gap:5px;margin-bottom:4px"><svg width="6" height="6" style="flex:none"><path d="M.5 3L2.5 5L5.5 .5" stroke="var(--blue)" fill="none" stroke-width=".8"/></svg><span>Praesent dictum rhoncus. Aenean ultrices, augue id tellus integer dolor, acque quis tincidunt, posuere nisi, neque sodales justo.</span></div>
      <div style="display:flex;gap:5px"><svg width="6" height="6" style="flex:none"><path d="M.5 3L2.5 5L5.5 .5" stroke="var(--blue)" fill="none" stroke-width=".8"/></svg><span>Nam auctor, leo a volutpat rhoncus, orci est gravida est in aliquet, vel mattis sem nulla.</span></div>
    </div>
    <div class="abs t" style="left:26px;right:40px;top:124px;font-size:3.6px;color:#777">Cras laoreet mauris eget lobortis auctor. Donec lacinia est id euismod eleifend. Quisque condimentum varius ullamcorper. Nunc quam libero, feugiat ut ante eu, ultrices eget ante.</div>
    <div class="brand">HARROW RIDGE</div>
  </section>

  <!-- 15 two column -->
  <section class="slide">
    <div class="edge"></div><div class="num">15</div>
    <div class="title">TWO COLUMN TEXT</div>
    <div class="abs lead" style="left:22px;right:22px;top:28px"><b>Contrary to popular belief,</b> Lorem Ipsum is not simply random text. It has roots in a piece of classical Latin literature from 45 BC. Cras laoreet mauris eget lobortis auctor. Donec lacinia est id euismod eleifend.</div>
    <div class="abs cols t" style="left:22px;right:22px;top:52px">
      <div>Lorem ipsum dolor sit amet, consectetur adipiscing elit. Etiam et nisl quis nulla eleifend tincidunt. Vestibulum dignissim arcu at sem porttitor, sed blandit lorem facilisis. Curabitur pretium ante in nibh pulvinar varius sed dictum libero. Donec aliquet nunc quis elit pharetra, sed laoreet mauris molestie. Quisque at ligula in nunc porta tincidunt.<br><br>Mauris vitae orci dolor. Aenean aliquet blandit leo, sed convallis elit lacinia quis. Nulla facilisi. Integer eget nibh sed augue tempus laoreet. Donec vitae leo quis neque pretium vehicula sit amet non lacus. Sed at odio varius, dapibus tellus id, varius quam.</div>
      <div>Nullam vel velit vitae lorem scelerisque volutpat non nec sapien. Phasellus tempus tortor eu nunc feugiat, nec pulvinar magna dapibus. Etiam sed nisl at erat dictum faucibus non vitae dolor. Donec vehicula dolor eget mi cursus mollis.<br><br>Aliquam hendrerit magna nec luctus vulputate. Suspendisse potenti. Vivamus varius nibh vel tortor placerat, sit amet vestibulum augue sagittis. Proin at massa congue, cursus leo et, gravida mi. Integer vitae sem vel diam sodales vulputate.</div>
    </div>
    <div class="brand">HARROW RIDGE</div>
  </section>

  <!-- 16 three column -->
  <section class="slide">
    <div class="edge"></div><div class="num">16</div>
    <div class="title">THREE COLUMN TEXT</div>
    <div class="abs lead" style="left:22px;right:22px;top:28px"><b>Contrary to popular belief,</b> Lorem Ipsum is not simply random text. It has roots in a piece of classical Latin literature from 45 BC. Cras laoreet mauris eget lobortis auctor. Donec lacinia est id euismod eleifend.</div>
    <div class="abs cols t" style="left:22px;right:22px;top:52px;gap:7px">
      <div>Lorem ipsum dolor sit amet, consectetur adipiscing elit. Etiam et nisl quis nulla eleifend tincidunt. Vestibulum dignissim arcu at sem porttitor, sed blandit lorem facilisis. Curabitur pretium ante in nibh pulvinar varius.<br><br>Sed dictum libero donec aliquet nunc quis elit pharetra, sed laoreet mauris molestie.</div>
      <div>Quisque at ligula in nunc porta tincidunt. Mauris vitae orci dolor. Aenean aliquet blandit leo, sed convallis elit lacinia quis. Nulla facilisi. Integer eget nibh sed augue tempus laoreet.<br><br>Donec vitae leo quis neque pretium vehicula sit amet non lacus. Sed at odio varius.</div>
      <div>Nullam vel velit vitae lorem scelerisque volutpat non nec sapien. Phasellus tempus tortor eu nunc feugiat, nec pulvinar magna dapibus.<br><br>Etiam sed nisl at erat dictum faucibus non vitae dolor. Donec vehicula dolor eget mi cursus mollis, aliquam hendrerit magna.</div>
    </div>
    <div class="brand">HARROW RIDGE</div>
  </section>

  <!-- 17 section break -->
  <section class="slide" style="background:var(--navy)">
    <div class="photo" role="img" aria-label="Photo of a hand holding a coffee cup on a wooden table" style="left:0;top:0;width:150px;bottom:0;background:linear-gradient(140deg,#5a4434,#8e7058 45%,#c9b9a8)"></div>
    <div class="abs" style="left:150px;top:0;width:8px;bottom:0;background:var(--blue)"></div>
    <div class="circ abs" style="left:203px;top:48px;width:16px;height:16px;border:.8px solid #fff"><svg width="3" height="9"><circle cx="1.5" cy="1" r="1" fill="#fff"/><rect x=".5" y="3" width="2" height="6" fill="#fff"/></svg></div>
    <div class="abs" style="left:162px;right:4px;top:84px;text-align:center;font:400 8px 'Raleway',sans-serif;color:#fff">Section Break</div>
    <div class="abs" style="left:172px;right:14px;top:98px;text-align:center;font-size:3px;line-height:1.4;color:#dfe6f0">The quick, brown fox jumps over a lazy dog. Six fuzzy foxes are watched quietly by two bold owls.</div>
    <div class="abs" style="left:6px;bottom:8px;font:700 4.6px 'Raleway',sans-serif;color:#fff">HARROW RIDGE</div>
  </section>

  <!-- 18 annual report -->
  <section class="slide">
    <div class="edge"></div><div class="num">18</div>
    <div class="title">ANNUAL REPORT TABLE</div>
    <div class="abs" style="left:14px;top:42px;display:flex;gap:5px">
      <div class="circ" style="width:15px;height:15px;border:.8px solid #222"><svg width="8" height="8"><path d="M1 1L7 7M7 1L1 7" stroke="#222"/></svg></div>
      <div class="circ" style="width:15px;height:15px;border:.8px solid #222"><svg width="6" height="8"><path d="M1 1h4L3 4v4" stroke="#222" fill="none"/></svg></div>
    </div>
    <div class="abs" style="left:83px;top:43px;font:700 4.4px 'Raleway',sans-serif;color:var(--blue)">Company budget files 2019</div>
    <div class="abs t" style="left:83px;top:50px;width:145px">Annual figures show a steady rise in revenue and margin over the period, with strong results in each region.</div>
    <div class="abs" style="left:14px;top:76px;width:214px;font-size:3.2px;color:#999">
      <div style="display:grid;grid-template-columns:2fr 1fr 1fr 1fr 1fr;color:var(--blue);border-bottom:.6px solid var(--blue);padding-bottom:1px"><span>Net revenue summary</span><span>2014</span><span>2015</span><span>2016</span><span>2017</span></div>
      <div class="bar-row"><span>Revenue, consolidated</span><span>4,451</span><span>4,451</span><span>4,451</span><span>4,451</span></div>
      <div class="bar-row"><span>Revenue, consolidated</span><span>5,565</span><span>5,565</span><span>5,565</span><span>5,565</span></div>
      <div class="bar-row"><span>Revenue, consolidated</span><span>6,950</span><span>6,950</span><span>6,950</span><span>6,950</span></div>
      <div class="bar-row"><span>Revenue, consolidated</span><span>7,955</span><span>7,955</span><span>7,955</span><span>7,955</span></div>
      <div class="bar-row"><span>Revenue, consolidated</span><span>8,759</span><span>8,759</span><span>8,759</span><span>8,759</span></div>
      <div style="color:var(--blue);padding-top:1.6px">CHANGE (%)</div>
    </div>
    <div class="abs" style="left:230px;top:42px;right:0;height:91px;background:var(--blue);font-size:3.6px;color:#e8f0fa">
      <div style="background:#111;color:#fff;padding:2.5px 8px;font-size:3.8px">STATS MANAGER</div>
      <div style="padding:4px 14px;border-bottom:.5px solid #86b0de">THIS YEAR<br>17,760</div>
      <div style="padding:4px 14px;border-bottom:.5px solid #86b0de">THIS MONTH<br>3,000</div>
      <div style="padding:4px 14px;border-bottom:.5px solid #86b0de">THIS WEEK<br>450</div>
      <div style="padding:4px 14px">TODAY<br>125</div>
    </div>
    <div class="brand">HARROW RIDGE</div>
  </section>

  <!-- 19 contact -->
  <section class="slide">
    <div class="edge"></div><div class="num">19</div>
    <div class="title">CONTACT US</div>
    <div class="abs" style="left:22px;top:28px;font-size:4.4px;color:#555">Need assistance or have a question? Let us help. Contact our office today.</div>
    <div class="abs" style="left:22px;right:38px;top:42px;border-top:.6px solid #888"></div>
    <div class="abs" style="left:22px;top:48px;display:flex;gap:4px">
      <div style="width:9px;height:9px;background:#222;display:flex;align-items:center;justify-content:center"><svg width="5" height="6"><path d="M2.5 6L.5 3a2 2 0 1 1 4 0Z" fill="#fff"/></svg></div>
      <div><p style="font:700 4px 'Raleway',sans-serif">Head Office</p><p class="t">Office address line one<br>Office address line two<br>City, State, Postcode</p></div>
    </div>
    <div class="abs" style="left:150px;top:48px;display:flex;gap:4px">
      <div style="width:9px;height:9px;background:var(--blue-light);display:flex;align-items:center;justify-content:center"><svg width="6" height="6"><circle cx="1.5" cy="3" r="1" fill="#fff"/><circle cx="4.5" cy="1.2" r="1" fill="#fff"/><circle cx="4.5" cy="4.8" r="1" fill="#fff"/><path d="M1.5 3L4.5 1.2M1.5 3L4.5 4.8" stroke="#fff" stroke-width=".5"/></svg></div>
      <div><p style="font:700 4px 'Raleway',sans-serif">Social Share</p><p class="t">● /harrowridge<br>● @harrowridge<br>● /harrowridge</p></div>
    </div>
    <div class="photo" role="img" aria-label="Photo of glass office building facade against blue sky with sunlight" style="left:6px;right:0;bottom:0;height:48px;background:linear-gradient(100deg,#2d4f7d 0%,#6f95c2 40%,#f3e3b7 70%,#8fb0d4 100%)"></div>
  </section>

  <!-- 20 thank you -->
  <section class="slide">
    <div class="abs" style="left:0;right:0;top:54px;text-align:center;font:600 8px 'Raleway',sans-serif;color:var(--blue)">Harrow Ridge Partners</div>
    <div class="abs" style="left:0;right:0;top:72px;text-align:center;font:700 10px 'Raleway',sans-serif;color:#666">Thank You</div>
    <div class="abs" style="left:32px;right:32px;top:88px;border-top:.8px solid var(--navy)"></div>
    <div class="abs t" style="left:58px;right:58px;top:94px;text-align:center">Thank you for your time and interest in our firm. We look forward to building lasting value together with every partner and investor.</div>
  </section>

</main>
</body>
</html>
```